MHT 25 year Anniversary - create file

I need an electronic Image file that I can incorporate into everything we are dong -including our pamphlets and brochures which we print in-house with Word Or Publisher files

The Vanto guide 25 file attached is the look we're after for part of our 25 year branding. I've included three of our different operating brands that should be incorporated into the letters. Other facts that can be included are :
123 combined years of experience
11792 Clients on file
11 Team Members
60% have been with us 5+ years
Service Entire Niagara Region
Carpet Cleaning
Oriental Rug Cleaning
Rug Binding
Making Custom Rugs
Winner of 8 Franchise Awards
Winner - Chamber of Commerce - "Summit Merit Honour"
Winner - Quillfen Promotions's "Climb past Limits " Award
Marisol and Tod featured in magazine article "Two Desks, One Home"
Supporters of the "Kids" programs at the KORB
Supporters of our Local Health System

Industry/Entity Type

Electronic

Colors
0255a3

Requirements
Must have
• final file must be a format that I can use to insert into other publications in Word and Publisher

```html
<!DOCTYPE html>
<html lang="en">
<head>
<meta charset="utf-8">
<title>MHT 25 Year Anniversary</title>
<link rel="stylesheet" href="https://fonts.googleapis.com/css2?family=Arimo:wght@400;700&display=swap">
<style>
  :root {
    --brand-blue: #1d4289;
    --tile-grey: #e2e2e4;
    --accent-red: #e22a1f;
    --copy-plum: #9a3f7c;
    --panel-white: #ffffff;
    --panel-rule: #c9c9c9;
    --brand-navy: #16367a;
    --brand-brown: #7a3b1e;
  }
  html, body {
    margin: 0;
    padding: 0;
    overflow: hidden;
    background: var(--brand-blue);
  }
  .anniversary-canvas {
    position: relative;
    width: 1200px;
    height: 893px;
    overflow: hidden;
    background: var(--brand-blue);
    font-family: "Arimo", Arial, sans-serif;
  }
  .numeral-art {
    position: absolute;
    left: 0;
    top: 0;
    display: block;
  }
  .digit { fill: var(--tile-grey); }
  .tile-gap {
    stroke: var(--brand-blue);
    stroke-width: 6;
    fill: none;
    stroke-linecap: round;
    stroke-linejoin: round;
  }
  .fact-head {
    fill: var(--accent-red);
    font-weight: 700;
  }
  .fact-copy {
    fill: var(--copy-plum);
    font-weight: 400;
  }
  .brand-strip {
    position: absolute;
    left: 10px;
    right: 10px;
    top: 740px;
    height: 143px;
    display: flex;
    gap: 20px;
  }
  .brand-panel {
    flex: 1;
    background: var(--panel-white);
    border-top: 2px solid var(--panel-rule);
    display: flex;
    align-items: center;
    justify-content: center;
    gap: 12px;
  }
  .brand-name {
    font-family: "Arimo", Arial, sans-serif;
    font-weight: 700;
    font-size: 28px;
    text-transform: uppercase;
    letter-spacing: 0.5px;
    text-align: center;
    line-height: 1.1;
  }
  .brand-name--floor { color: var(--brand-navy); }
  .brand-name--wash { color: var(--brand-brown); }
  .brand-name--studio { color: var(--brand-navy); }
  .brand-dot {
    width: 18px;
    height: 18px;
    border-radius: 50%;
    background: var(--brand-navy);
  }
</style>
</head>
<body>
<main class="anniversary-canvas">
  <svg class="numeral-art" width="1200" height="730" viewBox="0 0 1200 730" xmlns="http://www.w3.org/2000/svg">
    <!-- numeral two -->
    <path class="digit" d="M108 245 C110 120 220 45 340 45 C470 45 570 120 568 215 C566 300 530 345 462 422 L330 578 L568 578 L568 690 L108 690 L108 630 L300 395 C370 330 440 285 435 240 C430 185 390 150 335 150 C285 150 255 190 250 245 Z"/>
    <!-- numeral five -->
    <path class="digit" d="M705 65 L1070 65 L1070 180 L812 180 L806 265 C840 258 880 256 910 260 C1030 275 1104 370 1102 485 C1100 610 1000 700 862 700 C760 700 690 665 632 612 L632 528 L752 530 A105 105 0 1 0 777 420 L655 398 L655 300 L690 298 L692 160 L705 158 Z"/>

    <!-- tile divisions -->
    <g class="tile-gap">
      <polyline points="288,168 262,104 232,100"/>
      <line x1="405" y1="140" x2="532" y2="128"/>
      <line x1="428" y1="208" x2="572" y2="202"/>
      <line x1="296" y1="405" x2="464" y2="428"/>
      <line x1="226" y1="490" x2="390" y2="512"/>
      <line x1="342" y1="578" x2="295" y2="692"/>

      <line x1="880" y1="62" x2="900" y2="182"/>
      <polyline points="688,158 800,162 808,182"/>
      <line x1="652" y1="298" x2="808" y2="290"/>
      <line x1="808" y1="278" x2="848" y2="392"/>
      <line x1="910" y1="410" x2="1104" y2="405"/>
      <line x1="902" y1="590" x2="1082" y2="602"/>
      <line x1="775" y1="570" x2="800" y2="702"/>
    </g>

    <!-- numeral two facts -->
    <text class="fact-head" x="165" y="148" font-size="44">123</text>
    <text class="fact-copy" x="138" y="174" font-size="26">combined</text>
    <text class="fact-copy" x="120" y="207" font-size="24" font-weight="700">years</text>
    <text class="fact-copy" x="190" y="207" font-size="32">of</text>
    <text class="fact-copy" x="115" y="238" font-size="22">experience</text>

    <text class="fact-head" x="242" y="88" font-size="30">11792</text>
    <text class="fact-copy" x="326" y="96" font-size="36">Clients</text>
    <text class="fact-copy" x="282" y="126" font-size="30">on</text>
    <text class="fact-copy" x="330" y="140" font-size="44">file</text>

    <text class="fact-head" x="405" y="177" font-size="48">11</text>
    <text class="fact-copy" x="470" y="166" font-size="26">Team</text>
    <text class="fact-copy" x="430" y="198" font-size="26">Members</text>

    <text class="fact-head" x="440" y="262" font-size="44">60%</text>
    <text class="fact-copy" x="446" y="298" font-size="38">have</text>
    <text class="fact-copy" x="418" y="335" font-size="40">been</text>
    <text class="fact-copy" x="376" y="366" font-size="30">with us</text>
    <text class="fact-copy" x="374" y="400" font-size="34">5+</text>
    <text class="fact-copy" x="420" y="396" font-size="26">years</text>

    <text class="fact-head" x="278" y="456" font-size="32">Carpet</text>
    <text class="fact-copy" x="248" y="483" font-size="26">Cleaning</text>

    <text class="fact-head" x="194" y="546" font-size="28">Oriental</text>
    <text class="fact-copy" x="152" y="610" font-size="62">Rug</text>
    <text class="fact-copy" x="113" y="670" font-size="34">Cleaning</text>

    <text class="fact-head" x="350" y="600" font-size="22" letter-spacing="3">Service</text>
    <text class="fact-copy" x="343" y="640" font-size="40" letter-spacing="2">Entire</text>
    <text class="fact-copy" x="356" y="682" font-size="40">Niagara</text>
    <text class="fact-copy" x="0" y="0" font-size="28" transform="translate(552 688) rotate(-90)">Region</text>

    <!-- numeral five facts -->
    <text class="fact-head" x="728" y="98" font-size="32">Making</text>
    <text class="fact-copy" x="710" y="142" font-size="42">Custom</text>
    <text class="fact-copy" x="815" y="174" font-size="30">Rugs</text>

    <text class="fact-head" x="905" y="114" font-size="60" letter-spacing="8">Rug</text>
    <text class="fact-copy" x="918" y="168" font-size="40">Binding</text>

    <text class="fact-head" x="696" y="190" font-size="24">Winner</text>
    <text class="fact-copy" x="692" y="214" font-size="24">Chamber</text>
    <text class="fact-copy" x="692" y="245" font-size="34">of</text>
    <text class="fact-copy" x="726" y="240" font-size="16">Commerce</text>
    <text class="fact-copy" x="694" y="264" font-size="16">"Summit Merit</text>
    <text class="fact-copy" x="700" y="284" font-size="18">Honour"</text>

    <text class="fact-head" x="840" y="296" font-size="24">Winner</text>
    <text class="fact-copy" x="850" y="320" font-size="21" letter-spacing="3">Quillfen</text>
    <text class="fact-copy" x="852" y="347" font-size="27">Promotions's</text>
    <text class="fact-copy" x="872" y="376" font-size="28">"Climb past</text>
    <text class="fact-copy" x="940" y="402" font-size="24">Limits"</text>
    <text class="fact-copy" x="1030" y="402" font-size="14">Award</text>

    <text class="fact-head" x="667" y="331" font-size="32">Winner</text>
    <text class="fact-copy" x="660" y="361" font-size="28">of</text>
    <text class="fact-copy" x="690" y="361" font-size="22">8</text>
    <text class="fact-copy" x="706" y="361" font-size="22">Franchise</text>
    <text class="fact-copy" x="668" y="390" font-size="28">Awards</text>

    <text class="fact-head" x="960" y="434" font-size="22">Marisol</text>
    <text class="fact-copy" x="963" y="458" font-size="20">and Tod</text>
    <text class="fact-copy" x="963" y="488" font-size="32">featured</text>
    <text class="fact-copy" x="965" y="505" font-size="17">in magazine</text>
    <text class="fact-copy" x="962" y="538" font-size="40">article</text>
    <text class="fact-copy" x="955" y="560" font-size="18">"Two Desks,</text>
    <text class="fact-copy" x="950" y="583" font-size="22">One Home"</text>

    <text class="fact-head" x="640" y="550" font-size="17">Supporters</text>
    <text class="fact-copy" x="648" y="571" font-size="17">of the "Kids"</text>
    <text class="fact-copy" x="662" y="597" font-size="21">programs</text>
    <text class="fact-copy" x="662" y="623" font-size="18">at the</text>
    <text class="fact-copy" x="700" y="651" font-size="22">KORB</text>

    <text class="fact-head" x="805" y="622" font-size="22" letter-spacing="3">Supporters</text>
    <text class="fact-copy" x="842" y="650" font-size="26">of our Local</text>
    <text class="fact-copy" x="808" y="673" font-size="22">Health System</text>
  </svg>

  <section class="brand-strip" aria-label="Operating brands">
    <div class="brand-panel">
      <span class="brand-dot"></span>
      <span class="brand-name brand-name--floor">Steadfast<br>Floor Care</span>
    </div>
    <div class="brand-panel">
      <span class="brand-name brand-name--wash">Heritage Loom<br>Wash Co.</span>
    </div>
    <div class="brand-panel">
      <span class="brand-name brand-name--studio">The Woven<br>Studio</span>
    </div>
  </section>
</main>
</body>
</html>
```